professional business card

Professional business card with logo on one side, and underneath logo list:
- power
-data
-fibre optic
-isolar

On other side:
Marcus Webb
Owner
MOB 0432 958 720
marcus@vorn.com.au
www.vornelectrical.com.au

Please edit logo to just leave VORN

```html
<!DOCTYPE html>
<html lang="en">
<head>
<meta charset="utf-8">
<title>VORN Business Card</title>
<link rel="stylesheet" href="https://fonts.googleapis.com/css2?family=Montserrat:wght@400;500;700&display=swap">
<style>
  :root {
    --teal: #17928f;
    --teal-dark: #128683;
    --white: #ffffff;
    --card-white: #f4f4f4;
    --ink: #2b2b2b;
    --grey: #6f6f6f;
    --rule: #8a8a8a;
    --backdrop: #d9dadb;
  }
  * { margin: 0; padding: 0; box-sizing: border-box; }
  html, body {
    width: 1200px; height: 1021px; overflow: hidden;
    background: var(--backdrop);
    font-family: "Montserrat", sans-serif;
  }
  .canvas { position: relative; width: 1200px; height: 1021px; }
  .card {
    position: absolute; left: 300px; width: 600px; height: 366px; overflow: hidden;
    box-shadow: 0 10px 28px rgba(0,0,0,0.18);
  }
  .card--front { top: 110px; background: linear-gradient(135deg, var(--teal), var(--teal-dark)); }
  .card--back { top: 545px; background: linear-gradient(120deg, var(--white), var(--card-white)); }

  .front-brand {
    position: absolute; left: 0; right: 0; top: 108px; text-align: center; color: var(--white);
  }
  .front-brand .wordmark {
    font-weight: 700; font-size: 92px; letter-spacing: 4px; line-height: 1;
  }
  .front-brand .services {
    display: inline-block; margin-top: 10px; padding-top: 8px;
    border-top: 1.5px solid var(--white);
    font-weight: 400; font-size: 14px; letter-spacing: 3px;
  }

  .back-brand {
    position: absolute; right: 70px; top: 70px;
    font-weight: 700; font-size: 62px; letter-spacing: 3px; color: var(--teal); line-height: 1;
  }
  .person { position: absolute; left: 70px; top: 200px; }
  .person .name { font-weight: 700; font-size: 20px; color: var(--teal); letter-spacing: 0.5px; }
  .person .role { font-weight: 400; font-size: 15px; color: var(--ink); margin-top: 2px; }
  .accent-line {
    position: absolute; left: 0; top: 226px; width: 56px; height: 2px; background: var(--teal);
  }
  .contact-rule {
    position: absolute; left: 70px; right: 40px; top: 258px; height: 1.5px; background: var(--rule);
  }
  .contacts {
    position: absolute; left: 62px; right: 36px; top: 278px;
    display: flex; justify-content: space-between; align-items: center; gap: 10px;
    font-size: 12.5px; color: var(--ink);
  }
  .contacts .item { display: flex; align-items: center; gap: 5px; white-space: nowrap; }
  .contacts svg { width: 13px; height: 13px; flex: none; }
</style>
</head>
<body>
<div class="canvas">
  <section class="card card--front">
    <div class="front-brand">
      <div class="wordmark">VORN</div>
      <div class="services">POWER | DATA | FIBRE OPTIC | ISOLAR</div>
    </div>
  </section>

  <section class="card card--back">
    <div class="back-brand">VORN</div>
    <div class="accent-line"></div>
    <div class="person">
      <div class="name">MARCUS WEBB</div>
      <div class="role">OWNER</div>
    </div>
    <div class="contact-rule"></div>
    <div class="contacts">
      <div class="item">
        <svg viewBox="0 0 16 16" aria-hidden="true"><rect x="4" y="1" width="8" height="14" rx="1.5" fill="none" stroke="#17928f" stroke-width="1.4"/><line x1="7" y1="12.5" x2="9" y2="12.5" stroke="#17928f" stroke-width="1.4"/></svg>
        <span>0432 958 720</span>
      </div>
      <div class="item">
        <svg viewBox="0 0 16 16" aria-hidden="true"><rect x="1" y="3" width="14" height="10" fill="none" stroke="#17928f" stroke-width="1.4"/><polyline points="1,3 8,9 15,3" fill="none" stroke="#17928f" stroke-width="1.4"/></svg>
        <span>marcus@vorn.com.au</span>
      </div>
      <div class="item">
        <svg viewBox="0 0 16 16" aria-hidden="true"><circle cx="8" cy="8" r="6.5" fill="none" stroke="#17928f" stroke-width="1.3"/><ellipse cx="8" cy="8" rx="3" ry="6.5" fill="none" stroke="#17928f" stroke-width="1.1"/><line x1="1.5" y1="8" x2="14.5" y2="8" stroke="#17928f" stroke-width="1.1"/></svg>
        <span>www.vornelectrical.com.au</span>
      </div>
    </div>
  </section>
</div>
</body>
</html>
```